Production Company need business cards

Hello ! I need a business card for my production company called Framewild. I put the logo in the files ! This is a brand new production company, modern. We work in the digital industry and have a new and young vision of the content creation. I'll use this business card with a system integrated in it, it will be a digital business card (the type of business card you put behind a phone, and in the phone all your informations will be displayed. You need to respect the colors of the logo for the card (but you can interchange the logo colours to use a black card, or white card, or gold card... You have the .ai file in the files)
In the uploaded files, i puted 2 business card examples, you can see on the cards I just need at the back a small square for a QR code (you can fake it for now).
Target Market(s)
Online business
Industry/Entity Type
Video production
Contact Information for Business Card
Name of the company (Framewild) , my name (Lucien Marvaux) and the little square for QR code at the back
Look and feel
Each slider illustrates characteristics of the customer's brand and the style your logo design should communicate.

```html
<!DOCTYPE html>
<html lang="en">
<head>
<meta charset="utf-8">
<title>Framewild Business Card</title>
<link href="https://fonts.googleapis.com/css2?family=Montserrat:wght@400;500;700&display=swap" rel="stylesheet">
<style>
  :root {
    --bg: #e3e3e3;
    --card: #2a2a2b;
    --card-edge: #c9a827;
    --gold: #e2c04a;
    --white: #f4f4f4;
    --muted: #bdbdbd;
    --divider: #8a8a8a;
    --emboss-light: rgba(255,255,255,0.16);
    --emboss-dark: rgba(255,255,255,0);
  }
  * { box-sizing: border-box; margin: 0; padding: 0; }
  html, body {
    width: 1200px; height: 900px; overflow: hidden;
    background: var(--bg);
    font-family: "Montserrat", sans-serif;
  }
  .sheet {
    width: 1200px; height: 900px;
    display: flex; align-items: center; justify-content: center; gap: 48px;
  }
  .card {
    position: relative;
    width: 530px; height: 320px;
    background: var(--card);
    border-radius: 30px;
    box-shadow: 0 6px 0 var(--card-edge), 0 18px 30px rgba(0,0,0,0.18);
    overflow: hidden;
  }
  .brand-name {
    font-family: "Montserrat", sans-serif;
    font-weight: 500;
    color: var(--white);
    font-size: 40px;
    letter-spacing: 0.5px;
    white-space: nowrap;
  }
  /* front */
  .card-front .brand-name { position: absolute; left: 58px; top: 118px; }
  .card-front .divider {
    position: absolute; left: 300px; top: 78px;
    width: 1px; height: 170px;
    background: linear-gradient(to bottom, transparent, var(--divider) 30%, var(--divider) 70%, transparent);
  }
  .contact { position: absolute; left: 326px; top: 82px; color: var(--white); }
  .contact-name { color: var(--gold); font-weight: 700; font-size: 17px; white-space: nowrap; }
  .contact-role { color: var(--muted); font-size: 10px; letter-spacing: 0.6px; margin-top: 3px; }
  .contact-address { font-size: 11px; line-height: 1.45; margin-top: 8px; }
  .contact-list { list-style: none; margin-top: 8px; font-size: 11px; line-height: 1.6; }
  .contact-list li { display: flex; align-items: center; gap: 8px; }
  .contact-list svg { width: 11px; height: 11px; fill: var(--gold); flex: none; }
  /* back */
  .card-back .brand-name { position: absolute; left: 70px; top: 70px; }
  .emboss-motif {
    position: absolute; right: -20px; bottom: 40px;
    width: 330px; height: 90px;
    border-radius: 60px 10px 60px 10px;
    transform: rotate(-18deg);
    background: linear-gradient(to right, var(--emboss-dark), var(--emboss-light) 70%, rgba(255,255,255,0.06));
  }
  .qr-square {
    position: absolute; left: 70px; bottom: 48px;
    width: 76px; height: 76px;
    border: 2px solid var(--gold);
    border-radius: 6px;
    background: var(--white);
  }
</style>
</head>
<body>
<main class="sheet">
  <section class="card card-front" aria-label="Business card front">
    <div class="brand-name">Framewild</div>
    <div class="divider"></div>
    <div class="contact">
      <p class="contact-name">Lucien Marvaux</p>
      <p class="contact-role">FOUNDER &amp; CEO</p>
      <p class="contact-address">2146 Alderwick Road<br>Fairbury, Ohio 40128</p>
      <ul class="contact-list">
        <li><svg viewBox="0 0 24 24" aria-hidden="true"><path d="M6.6 10.8a15 15 0 0 0 6.6 6.6l2.2-2.2c.3-.3.7-.4 1-.2 1.1.4 2.3.6 3.6.6.6 0 1 .4 1 1V20c0 .6-.4 1-1 1A17 17 0 0 1 3 4c0-.6.4-1 1-1h3.5c.6 0 1 .4 1 1 0 1.3.2 2.5.6 3.6.1.3 0 .7-.2 1z"/></svg>555-218-4670</li>
        <li><svg viewBox="0 0 24 24" aria-hidden="true"><path d="M7 1h10a2 2 0 0 1 2 2v18a2 2 0 0 1-2 2H7a2 2 0 0 1-2-2V3a2 2 0 0 1 2-2zm0 3v14h10V4zm5 15.5a1 1 0 1 0 0 2 1 1 0 0 0 0-2z"/></svg>555-309-7182</li>
        <li><svg viewBox="0 0 24 24" aria-hidden="true"><path d="M6 2h9l3 3v5h1a3 3 0 0 1 3 3v7h-4v2H6v-2H2v-7a3 3 0 0 1 3-3h1zm2 2v6h8V6h-2V4zm0 12v4h8v-4z"/></svg>555-742-0935</li>
        <li><svg viewBox="0 0 24 24" aria-hidden="true"><path d="M2 5h20v14H2zm2 2v.5l8 5 8-5V7zm0 2.8V17h16V9.8l-8 5z"/></svg>info@framewild.com</li>
        <li><svg viewBox="0 0 24 24" aria-hidden="true"><path d="M12 2a10 10 0 1 0 0 20 10 10 0 0 0 0-20zm6.9 9h-3a15 15 0 0 0-1.3-5.6A8 8 0 0 1 18.9 11zM12 4.1c.9 1.3 1.8 3.6 1.9 6.9h-3.8c.1-3.3 1-5.6 1.9-6.9zM9.4 5.4A15 15 0 0 0 8.1 11h-3a8 8 0 0 1 4.3-5.6zM5.1 13h3a15 15 0 0 0 1.3 5.6A8 8 0 0 1 5.1 13zm6.9 6.9c-.9-1.3-1.8-3.6-1.9-6.9h3.8c-.1 3.3-1 5.6-1.9 6.9zm2.6-1.3a15 15 0 0 0 1.3-5.6h3a8 8 0 0 1-4.3 5.6z"/></svg>www.framewild.com</li>
      </ul>
    </div>
  </section>

  <section class="card card-back" aria-label="Business card back">
    <div class="brand-name">Framewild</div>
    <div class="emboss-motif" role="img" aria-label="Faint embossed decorative motif in dark gloss"></div>
    <div class="qr-square" role="img" aria-label="Space for QR code"></div>
  </section>
</main>
</body>
</html>
```